Brochure Design

We are looking for a brochure design that describes our credit repair and restoration business.
One of the files that has been uploaded is "TRV Presentation Guidebook". This provides information about our service and snippets can be used for the text in the brochure.
I also uploaded several examples of brochures that we liked.
Target Market(s)
The target market is consumers, not businesses, who are considering our credit repair and restoration service.
Industry/Entity Type
Business
Requirements
Must have
- We want a brochure that is rich with color, and pictures of families and business people. Large pictures that span the entire length of the brochure, or several panels is preferred. The color scheme should be black and blue based
Nice to have
- A stylized representation of our logo. Our logo is not important to be included in the primary design scheme, because our logo is not stylistic enough from what we currently have. However, a stylized version of our logo that can be integrated into the design in some way would be wonderful. We will attached a pic of our design. It is pretty basic and there are many stock photos or art that can be used to offer a more stylized version of our logo to incorporate into the design.
Should not have
- The primary focus of the brochure is a professional design with plenty of color and pictures. This is not designed to necessarily be an informative brochure, but more of a "business presence" brochure. So there is not a need to provide a lot of space for text. Certainly there should be enough text to describe our business and make some bullet points, but text explanation is not the focus.

```html
<!DOCTYPE html>
<html lang="en">
<head>
<meta charset="utf-8">
<title>TRV Credit Brochure</title>
<link href="https://fonts.googleapis.com/css2?family=Arimo:wght@400;700&display=swap" rel="stylesheet">
<style>
:root{
  --teal:#4fb3a3;
  --teal-deep:#3fa395;
  --slate-teal:#4c6e6c;
  --paper:#e7e7e7;
  --ink:#000;
  --white:#fff;
  --gold:#f6c312;
  --photo-dark:#3b3b36;
  --photo-mid:#8a8a7e;
}
*{box-sizing:border-box;margin:0;padding:0}
html,body{width:1200px;height:847px;overflow:hidden;background:var(--white)}
body{font-family:"Arimo",Arial,sans-serif;color:var(--ink)}
.brochure{position:relative;width:1200px;height:847px}
.panel{position:absolute;overflow:hidden}

/* Enrollment steps */
.enroll{left:0;top:0;width:405px;height:318px;background:var(--teal);color:var(--white);padding:50px 36px 0 52px}
.enroll__intro{font-size:14.5px;line-height:1.33}
.steps{list-style:none;margin-top:18px;font-size:15px}
.step{display:flex;align-items:flex-start;gap:10px;margin-bottom:12px}
.step__num{flex:none;width:27px;height:27px;border-radius:50%;background:var(--ink);color:var(--white);font-weight:700;font-size:19px;display:flex;align-items:center;justify-content:center}
.step__text{padding-top:4px;line-height:1.3}
.step--1{margin-left:14px}
.step--2{margin-left:38px}
.step--3{margin-left:22px}

/* Fees */
.fees{left:405px;top:0;width:388px;height:318px;background:var(--paper);text-align:center}
.fees__title{font-size:27px;font-weight:400;line-height:1.24;margin-top:37px}
.fee-table{border-collapse:collapse;margin:20px 0 0 16px;font-size:12px}
.fee-table th,.fee-table td{padding:6px 4px;border:1px solid #333;font-weight:400;text-align:left}
.fee-table .row-label{border:none;font-size:10.5px;padding-right:4px}
.fee-table .corner{border:none}
.fees__note{font-size:10.5px;line-height:1.35;text-align:justify;margin:20px 54px 0 52px}

/* Photo areas */
.photo-family{left:793px;top:0;width:407px;height:318px;background:linear-gradient(120deg,#2a2a2a 0%,#6e6e6e 45%,#b9b9b9 60%,#3a3a3a 100%)}
.photo-team{left:0;top:318px;width:793px;height:312px;background:linear-gradient(160deg,#5d5f4a 0%,var(--photo-mid) 35%,#cfcfc6 55%,var(--photo-dark) 100%)}
.photo-word{position:absolute;font-weight:400;letter-spacing:-2px;line-height:1}
.photo-word--freedom{top:6px;left:4px;font-size:86px;color:rgba(200,200,200,.55)}
.photo-word--credit{bottom:16px;left:14px;font-size:84px;color:rgba(140,140,140,.8)}

/* Slogan */
.slogan{left:793px;top:318px;width:407px;height:312px;background:var(--teal-deep);color:var(--ink)}
.slogan__big{position:absolute;left:22px;top:6px;font-size:84px;color:var(--white);letter-spacing:-1px}
.slogan__sub{position:absolute;left:27px;top:86px;font-size:40px}
.slogan__lead{position:absolute;left:27px;top:158px;font-size:25px}
.slogan__gold{position:absolute;left:27px;top:185px;font-size:33px;color:var(--gold)}
.slogan__us{position:absolute;right:62px;top:212px;font-size:74px;color:var(--white)}

/* Benefits */
.benefits{left:0;top:630px;width:793px;height:217px;background:var(--ink);color:var(--white);font-size:11.2px;line-height:1.55;padding:14px 30px 0 47px;display:flex;gap:54px}
.benefits__col{width:334px;text-align:justify}
.benefits strong{font-weight:700}
.benefits ul{list-style:none;margin-top:2px}
.benefits li{padding-left:26px;text-indent:-12px}
.benefits li::before{content:"-";margin-right:7px}

/* Brand + contact */
.brand{left:793px;top:630px;width:407px;height:122px;background:var(--white);display:flex;align-items:center;justify-content:center;gap:12px}
.brand__mark{width:30px;height:30px;background:var(--teal)}
.brand__name{font-size:30px;font-weight:700;color:var(--teal)}
.contact{left:793px;top:752px;width:407px;height:95px;background:var(--slate-teal);color:var(--white);font-size:10.2px;line-height:1.45;text-align:center;padding-top:16px}
</style>
</head>
<body>
<div class="brochure">

  <section class="panel enroll">
    <p class="enroll__intro">Now that you heard all of the details about our program, the only step remaining is to sign-up. Please complete the following steps to enroll in our credit repair and restoration program.</p>
    <ol class="steps">
      <li class="step step--1"><span class="step__num">1</span><span class="step__text">Complete the Client Enrollment Form</span></li>
      <li class="step step--2"><span class="step__num">2</span><span class="step__text">Send us a copy of your<br>&nbsp;&nbsp;&nbsp;&nbsp;Driver's License.</span></li>
      <li class="step step--3"><span class="step__num">3</span><span class="step__text">You must sign-up for a credit monitoring account if you don't<br>&nbsp;&nbsp;&nbsp;have one allready</span></li>
    </ol>
  </section>

  <section class="panel fees">
    <h2 class="fees__title">Schedule of<br>Fees and Services</h2>
    <table class="fee-table">
      <tr><th class="corner"></th><th>Setup</th><th>Month 1</th><th>Month 2</th><th>Month 3</th><th>Month 4</th><th>Total</th></tr>
      <tr><td class="row-label">Single</td><td>$299</td><td>$129</td><td>$129</td><td>$129</td><td>$129</td><td>$815</td></tr>
      <tr><td class="row-label">Couple</td><td>$459</td><td>$189</td><td>$189</td><td>$189</td><td>$189</td><td>$1,215</td></tr>
    </table>
    <p class="fees__note">You will be provided with a Client Web Portal, which is a website where you can login 24/7 and get real-time results of your credit repair program. You simply go to our website, www.TRVCredit.com, and put in your own username and password.</p>
  </section>

  <div class="panel photo-family" role="img" aria-label="Photo of a mother kissing her smiling daughter">
    <span class="photo-word photo-word--freedom">freedom</span>
  </div>

  <div class="panel photo-team" role="img" aria-label="Photo of two young professionals smiling at a laptop outdoors">
    <span class="photo-word photo-word--credit">creditworthy</span>
  </div>

  <section class="panel slogan">
    <span class="slogan__big">Be free</span>
    <span class="slogan__sub">to live your life</span>
    <span class="slogan__lead">and leave your</span>
    <span class="slogan__gold">bad credit worries</span>
    <span class="slogan__us">to us</span>
  </section>

  <section class="panel benefits">
    <div class="benefits__col">
      <p><strong>Our objective for all of our clients is to get them to a 700 credit score or above.</strong> 700 is the average credit score in the United States 1/2 of the country is above 700 and the other half is below. With a credit score around 700 you can:</p>
      <ul>
        <li>Get a VA, FHA or even Conventional mortgage to purchase a primary, investment or 2nd home.</li>
        <li>Get a major credit card with a high limit and low interest rate</li>
        <li>Qualify for credit to purchase large ticket items like</li>
      </ul>
    </div>
    <div class="benefits__col">
      <ul>
        <li style="text-indent:0;padding-left:26px">furniture, appliances, home improvement, etc.</li>
        <li>Rent the apartment you want without paying extra security deposits or fees.</li>
        <li>Buy a new or used car with the lowest interest rates possible, and without compromising what you want due to credit</li>
      </ul>
      <p><strong>The bottom line is that having a higher credit score means living without compromises or limitations caused by a low credit score.</strong></p>
    </div>
  </section>

  <section class="panel brand">
    <span class="brand__mark"></span>
    <span class="brand__name">TRV Credit</span>
  </section>

  <address class="panel contact" style="font-style:normal">
    2480 Harbor Line Road, Suite B, Fairview, MD 21000<br>
    Email: office@trvcredit.com | Web: www.TRVCredit.com<br>
    Toll Free: (800)555-0142 | Local: (410)555-0187 | Fax: (800)555-0163
  </address>

</div>
</body>
</html>
```